kestrel home systems HERS

Looking for business card design that represents our company. we are kestrel home systems and we dedicate our skills of home energy efficiency to our customer by providing energy solution to their energy problems.
HVAC
SOLAR
INSULLATION
LIGHTING
DUCT TESTING
HERS RATING.

```html
<!DOCTYPE html>
<html lang="en">
<head>
<meta charset="utf-8">
<title>Kestrel Home Systems – Business Card</title>
<link rel="stylesheet" href="https://fonts.googleapis.com/css2?family=Montserrat:wght@400;600;800&display=swap">
<style>
  :root {
    --stage: #2a2a2a;
    --card: #050505;
    --lime: #8cc63f;
    --lime-dim: #5e8a26;
    --sky: #3fa9dc;
    --grey: #bdbdbd;
    --white: #eeeeee;
  }
  * { box-sizing: border-box; margin: 0; padding: 0; }
  html, body {
    width: 1200px; height: 997px; overflow: hidden;
    background: var(--stage);
    font-family: "Montserrat", Arial, sans-serif;
  }
  .stage { position: relative; width: 1200px; height: 997px; }

  .card {
    position: absolute;
    width: 525px; height: 300px;
    background: var(--card);
    border: 2px solid var(--lime);
    border-radius: 26px;
    box-shadow: 0 0 14px rgba(140,198,63,0.35), 0 18px 40px rgba(0,0,0,0.6);
  }
  .card--front { left: 70px; top: 150px; }
  .card--back  { left: 605px; top: 500px; }

  .brand-frame {
    position: absolute;
    left: 50%; transform: translateX(-50%);
    top: 36px;
    width: 400px; height: 104px;
    border: 2px solid var(--lime);
    border-radius: 10px;
    display: flex; align-items: center; justify-content: center; gap: 14px;
  }
  .brand-dot {
    width: 30px; height: 30px; border-radius: 50%;
    background: var(--sky);
    flex: none;
  }
  .brand-name {
    color: var(--lime);
    font-weight: 800;
    font-size: 27px;
    letter-spacing: 0.5px;
    text-transform: uppercase;
    line-height: 1.05;
  }

  /* front */
  .holder {
    position: absolute; left: 62px; top: 190px;
  }
  .holder-name {
    color: var(--lime); font-weight: 800; font-size: 17px; letter-spacing: 0.5px;
  }
  .holder-title {
    color: var(--grey); font-size: 14px; margin-top: 4px; padding-left: 40px;
  }
  .divider {
    position: absolute; left: 282px; top: 180px;
    width: 1px; height: 64px; background: var(--lime-dim);
  }
  .contacts {
    position: absolute; left: 302px; top: 174px;
    list-style: none;
  }
  .contacts li {
    display: flex; align-items: center; gap: 10px;
    color: var(--grey); font-size: 12px; height: 24px;
  }
  .contacts svg { width: 16px; height: 16px; flex: none; }

  /* back */
  .services {
    position: absolute; left: 48px; top: 182px;
    display: grid; grid-template-columns: 130px 175px 170px;
    row-gap: 4px;
    list-style: none;
  }
  .services li {
    color: var(--lime); font-weight: 800; font-size: 17px;
    display: flex; align-items: center; gap: 8px;
    text-transform: uppercase;
  }
  .services li::before {
    content: ""; width: 8px; height: 8px; border-radius: 50%;
    background: var(--sky); flex: none;
  }
</style>
</head>
<body>
<main class="stage">

  <section class="card card--front" aria-label="Business card front">
    <div class="brand-frame">
      <span class="brand-dot"></span>
      <span class="brand-name">Kestrel<br>Home Systems</span>
    </div>
    <div class="holder">
      <p class="holder-name">MARLENE OSTERBY</p>
      <p class="holder-title">Board Certified</p>
    </div>
    <div class="divider"></div>
    <ul class="contacts">
      <li>
        <svg viewBox="0 0 16 16"><circle cx="8" cy="8" r="8" fill="#8cc63f"/><path d="M5.5 4.5l1.5 0 .7 2-1 .8a5 5 0 0 0 2 2l.8-1 2 .7v1.5c0 .5-.5 1-1 1A6 6 0 0 1 4.5 5.5c0-.5.5-1 1-1z" fill="#050505"/></svg>
        (555) 201-4417
      </li>
      <li>
        <svg viewBox="0 0 16 16"><circle cx="8" cy="8" r="8" fill="#8cc63f"/><rect x="4" y="5" width="8" height="6" rx="1" fill="#050505"/><rect x="5.5" y="3.5" width="5" height="2" fill="#050505"/></svg>
        (555) 201-9382
      </li>
      <li>
        <svg viewBox="0 0 16 16"><circle cx="8" cy="8" r="8" fill="#8cc63f"/><rect x="4" y="5" width="8" height="6" fill="#050505"/><path d="M4 5l4 3.5L12 5" stroke="#8cc63f" stroke-width="1" fill="none"/></svg>
        mosterby@kestrelhome.com
      </li>
    </ul>
  </section>

  <section class="card card--back" aria-label="Business card back">
    <div class="brand-frame">
      <span class="brand-dot"></span>
      <span class="brand-name">Kestrel<br>Home Systems</span>
    </div>
    <ul class="services">
      <li>HVAC</li>
      <li>Solar</li>
      <li>Insullation</li>
      <li>Lighting</li>
      <li>Duct Testing</li>
      <li>HERS Rating.</li>
    </ul>
  </section>

</main>
</body>
</html>
```